Create a Brochure Design for Brantley Homecare

Brantley Homecare is a subsidiary of the Brantley Care Group. This brochure is specifically for the Brantley Homecare company and brand. Create a 3 panel, A4, front and back, tri-fold brochure. This brochure will be a way to introduce our Homecare services to the community, prospective clients, and various referral partners. The brochure must be eye catching, unique in its deliverables and demonstrate both attention to detail and comfort. Our organization is sophisticated and built around warmth, care and individualized personal attention. The most important aspect of this design is to focus on creating a nurturing, warm, and inviting feel where you would want to have a Nurse or Nurse’s Aide in your own home or a loved one’s home.

I am open to the creativity of the designer to develop something based on the above criteria; however I would like the design to work well with the existing collateral material. What I mean by that is that while I want everything to have its own personality and stand out as its own brand representative, I still need to be able to tell that the overall design concept stays stylistically inside of the same ‘family’ of existing designed material. Because of this, below I would like for the designer to pull inspiration from the link to our website (Located below) as well as from the attachment of our recently refreshed business cards (Attached). This should allow each design to be unique and creative, while still staying inside of a framework and the feel/style that I am looking for.

Finally, I want all the designers to understand that this brochure design is for a private, in home, healthcare company where we are responsible for providing personalized care for a culturally and ethnically diverse make-up clientele of all ages. The photos that are used must represent an image of warmth, care, and a positive interaction between client and caregiver.

Look under the Brantley Homecare tab at www.brantleycaregroup-example.net

Industry/Entity Type

Healthcare

Requirements
Must have
• • The Brantley Homecare company logo must be included.

```html
<!DOCTYPE html>
<html lang="en">
<head>
<meta charset="utf-8">
<title>Brantley Homecare – Brochure Outer Spread</title>
<link rel="stylesheet" href="https://fonts.googleapis.com/css2?family=Sorts+Mill+Goudy:ital@0;1&family=Arimo:ital@0;1&display=swap">
<style>
  :root {
    --salmon: #d4957f;
    --sage: #b3d1a8;
    --teal: #1d5e52;
    --rule: #2c3a28;
    --white: #ffffff;
    --ink: #1a1a1a;
    --frame-grey: #9a9a9a;
  }
  * { box-sizing: border-box; margin: 0; padding: 0; }
  html, body { width: 1200px; height: 849px; overflow: hidden; background: var(--white); }
  .spread { position: relative; width: 1200px; height: 849px; overflow: hidden; background: var(--white); }

  .band { position: absolute; top: 347px; height: 502px; background: var(--salmon); }
  .band--back { left: 0; width: 400px; }
  .band--cover { left: 800px; width: 400px; }

  /* Back panel */
  .est-badge {
    position: absolute; left: 113px; top: 36px; width: 156px; height: 72px;
    border: 2px dotted var(--frame-grey); padding: 4px; background: var(--white);
  }
  .est-badge__inner {
    width: 100%; height: 100%; border: 1px solid var(--frame-grey);
    display: flex; align-items: center; justify-content: center;
    font-family: "Sorts Mill Goudy", Georgia, serif; font-style: italic;
    font-size: 25px; letter-spacing: 1.5px; color: #222;
  }

  .values-card {
    position: absolute; left: 20px; top: 143px; width: 353px; height: 428px;
    background: var(--sage); border: 6px solid var(--white);
    box-shadow: 0 1px 4px rgba(0,0,0,0.25);
  }
  .values-card__corners { position: absolute; left: -10px; top: -10px; width: 373px; height: 448px; pointer-events: none; }
  .values-card__mark {
    position: absolute; left: 143px; top: 12px; width: 50px; height: 48px;
    border-radius: 6px; background: var(--salmon);
  }
  .values-card__title {
    position: absolute; left: 0; right: 0; top: 80px; text-align: center;
    font-family: "Sorts Mill Goudy", Georgia, serif; font-weight: 400; font-size: 42px; line-height: 1; white-space: nowrap;
  }
  .values-card__title em { font-style: italic; color: var(--white); }
  .values-card__title strong { font-weight: 400; color: var(--teal); font-size: 46px; margin: 0 2px; }
  .values-card__rules { position: absolute; left: 0; top: 0; width: 341px; height: 416px; }
  .value {
    position: absolute; left: 0; right: 0; text-align: center;
    font-family: "Sorts Mill Goudy", Georgia, serif; font-style: italic;
    font-size: 31px; letter-spacing: 1.2px; color: var(--white); line-height: 1;
  }

  .tagline {
    position: absolute; left: 0; width: 400px; top: 592px; text-align: center;
    font-family: Arimo, Arial, sans-serif; font-style: italic; font-size: 20px;
    line-height: 27px; letter-spacing: 0.5px; color: var(--white);
  }

  .contact-card {
    position: absolute; left: 92px; top: 716px; width: 207px; height: 106px;
    border: 6px solid var(--white); background: var(--salmon);
    box-shadow: 0 3px 5px rgba(0,0,0,0.3);
    font-family: Arimo, Arial, sans-serif; font-style: normal; font-size: 15px; line-height: 19px;
    color: var(--white); text-align: center; padding-top: 6px; white-space: nowrap; overflow: hidden;
  }
  .contact-card__line--italic { font-style: italic; }

  /* Middle panel: mailing address */
  .mailer-address {
    position: absolute; left: 690px; top: 22px;
    writing-mode: vertical-rl; font-style: normal;
    font-family: Arimo, Arial, sans-serif; font-size: 17.5px; line-height: 24px; color: var(--ink);
  }

  /* Cover panel */
  .brand-mark {
    position: absolute; left: 941px; top: 113px; width: 112px; height: 108px;
    border-radius: 12px; background: var(--salmon);
  }
  .brand-name {
    position: absolute; left: 800px; width: 400px; top: 244px; text-align: center;
    font-family: "Sorts Mill Goudy", Georgia, serif; font-weight: 400; color: var(--teal);
  }
  .brand-name__primary { display: block; font-size: 92px; line-height: 100px; }
  .brand-name__secondary { display: block; font-size: 25px; letter-spacing: 14px; line-height: 28px; margin-top: 4px; padding-left: 14px; color: var(--white); }
</style>
</head>
<body>
<main class="spread">
  <div class="band band--back"></div>
  <div class="band band--cover"></div>

  <!-- Back panel -->
  <div class="est-badge"><div class="est-badge__inner">est. 1996</div></div>

  <section class="values-card">
    <svg class="values-card__corners" viewBox="0 0 373 448" aria-hidden="true">
      <g fill="#555">
        <polygon points="0,0 20,0 20,6 6,6 6,20 0,20"/>
        <polygon points="373,0 353,0 353,6 367,6 367,20 373,20"/>
        <polygon points="0,448 20,448 20,442 6,442 6,428 0,428"/>
        <polygon points="373,448 353,448 353,442 367,442 367,428 373,428"/>
      </g>
    </svg>
    <div class="values-card__mark" aria-hidden="true"></div>
    <h2 class="values-card__title"><em>the</em><strong>Brantley</strong><em>way</em></h2>
    <svg class="values-card__rules" viewBox="0 0 341 416" aria-hidden="true">
      <g stroke="var(--rule)" stroke-width="1.5" fill="var(--rule)">
        <line x1="40" y1="137" x2="297" y2="137"/>
        <line x1="40" y1="197" x2="297" y2="197"/>
        <line x1="40" y1="260" x2="297" y2="260"/>
        <line x1="40" y1="324" x2="297" y2="324"/>
        <line x1="40" y1="390" x2="297" y2="390"/>
        <g stroke="none">
          <polygon points="36,137 40,133 44,137 40,141"/><polygon points="293,137 297,133 301,137 297,141"/>
          <polygon points="36,197 40,193 44,197 40,201"/><polygon points="293,197 297,193 301,197 297,201"/>
          <polygon points="36,260 40,256 44,260 40,264"/><polygon points="293,260 297,256 301,260 297,264"/>
          <polygon points="36,324 40,320 44,324 40,328"/><polygon points="293,324 297,320 301,324 297,328"/>
          <polygon points="36,390 40,386 44,390 40,394"/><polygon points="293,390 297,386 301,390 297,394"/>
        </g>
      </g>
    </svg>
    <p class="value" style="top:145px">compassionate</p>
    <p class="value" style="top:210px">professional</p>
    <p class="value" style="top:274px">dependable</p>
    <p class="value" style="top:337px">flexible</p>
  </section>

  <p class="tagline">Someone you can depend on...<br>Without question.</p>

  <address class="contact-card">
    <div>brantleyhc.example</div>
    <div class="contact-card__line--italic">phone 808-555-0142</div>
    <div class="contact-card__line--italic">fax 808-555-0187</div>
    <div class="contact-card__line--italic">info@brantleyhc.example</div>
  </address>

  <!-- Middle panel -->
  <address class="mailer-address">
    Brantley Homecare<br>
    1450 Palm Crest Ave. Suite #210<br>
    Honolulu, HI 96815
  </address>

  <!-- Cover panel -->
  <div class="brand-mark" aria-hidden="true"></div>
  <h1 class="brand-name">
    <span class="brand-name__primary">Brantley</span>
    <span class="brand-name__secondary">HOMECARE</span>
  </h1>
</main>
</body>
</html>
```